Business Card Design Project

We need a business card to reflect the design of our website - just so it all ties in - it has a retro feel and can be found at http://www.velorasoulpair.com
We will need our phone 0437 215 964
Web address, and email velorapair@fernmail.com included
Our catch cry is "Classic Cocktail Music"
Perfect Live Music for Private & Corporate Events, Weddings and Dinner Music
Our names should be included :-
Maribel Thorne / piano & Dennis Holloway / bass
I am now also including our logo so that it can be included (in part or whole) somehow in the design
My partner thinks we should include our logo in some form in the design of the card - i will attach this here for you. I will attach eps but if you prefer another format please let me know
Regards
Mari

```html
<!DOCTYPE html>
<html lang="en">
<head>
<meta charset="utf-8">
<title>Velora Duo – Business Card</title>
<link rel="stylesheet" href="https://fonts.googleapis.com/css2?family=Josefin+Sans:wght@300;400&family=Raleway:wght@300;400&display=swap">
<style>
  :root {
    --page-bg: #e9e9ea;
    --card-teal: #8fbcbf;
    --stitch: #5f7577;
    --ink: #5a6465;
    --cream: #f4ecd6;
    --ribbon: #efe5c9;
    --ribbon-ink: #6b5f45;
    --badge: #5d6162;
    --photo-a: #f0c432;
    --photo-b: #e0457a;
    --photo-c: #4a63b5;
    --photo-d: #2b2230;
  }
  * { margin: 0; padding: 0; box-sizing: border-box; }
  html, body {
    width: 1200px; height: 825px; overflow: hidden;
    background: var(--page-bg);
  }
  .sheet {
    position: relative; width: 1200px; height: 825px;
  }
  .card {
    position: absolute; top: 272px;
    width: 496px; height: 286px;
    background: var(--card-teal);
    overflow: hidden;
  }
  .card--front { left: 66px; }
  .card--back { left: 624px; }
  .stitch {
    position: absolute; left: 0; right: 0;
    border-top: 1.5px dashed var(--stitch);
  }
  .stitch--top { top: 10px; }
  .stitch--bottom { bottom: 10px; }
  .glass-photo {
    position: absolute; left: 0; top: 0; bottom: 0;
    width: 170px;
    border-radius: 0 55% 45% 0 / 0 50% 50% 0;
    background:
      radial-gradient(circle at 30% 25%, var(--photo-a) 0 18%, transparent 40%),
      radial-gradient(circle at 60% 55%, var(--photo-b) 0 22%, transparent 50%),
      radial-gradient(circle at 25% 75%, var(--photo-c) 0 15%, transparent 40%),
      linear-gradient(160deg, var(--photo-b), var(--photo-c) 60%, var(--photo-d));
  }
  .card--back .glass-photo { width: 150px; }
  .brand-mark {
    position: absolute; left: 240px; top: 26px;
    width: 96px; height: 96px; border-radius: 50%;
    background: var(--badge);
  }
  .brand-name {
    position: absolute; left: 0; right: 0; top: 134px;
    text-align: center; padding-left: 80px;
    font-family: "Josefin Sans", sans-serif; font-weight: 400;
    font-size: 50px; letter-spacing: 1px;
    color: var(--cream);
  }
  .tagline-ribbon {
    position: absolute; left: 150px; top: 205px;
    width: 210px; height: 22px;
    background: var(--ribbon);
    display: flex; align-items: center; justify-content: center;
    font-family: "Josefin Sans", sans-serif; font-size: 11px;
    letter-spacing: 1.5px; color: var(--ribbon-ink);
  }
  .tagline-ribbon::before, .tagline-ribbon::after {
    content: ""; position: absolute; top: 3px;
    border: 8px solid var(--ribbon);
    border-left-color: transparent;
  }
  .tagline-ribbon::before { left: -12px; }
  .tagline-ribbon::after { right: -12px; transform: scaleX(-1); }
  .contact {
    position: absolute; left: 164px; top: 70px;
    font-family: "Raleway", sans-serif; font-weight: 300;
    color: var(--ink);
  }
  .contact__phone { font-size: 34px; letter-spacing: 1px; margin-bottom: 18px; }
  .contact__line { font-size: 16px; margin-bottom: 12px; margin-left: 16px; }
  .services {
    position: absolute; left: 108px; right: 10px; top: 253px;
    text-align: center;
    font-family: "Raleway", sans-serif; font-size: 9.5px;
    color: var(--ink);
  }
</style>
</head>
<body>
<main class="sheet">
  <section class="card card--front">
    <div class="stitch stitch--top"></div>
    <div class="glass-photo" role="img" aria-label="Colourful photo of a cocktail glass"></div>
    <div class="brand-mark"></div>
    <h1 class="brand-name">VELORA DUO</h1>
    <p class="tagline-ribbon">CLASSIC COCKTAIL MUSIC</p>
    <div class="stitch stitch--bottom"></div>
  </section>

  <section class="card card--back">
    <div class="stitch stitch--top"></div>
    <div class="glass-photo" role="img" aria-label="Colourful photo of a cocktail glass"></div>
    <div class="contact">
      <p class="contact__phone">0437 215 964</p>
      <p class="contact__line">velorapair@fernmail.com</p>
      <p class="contact__line">www.velorasoulpair.com</p>
    </div>
    <p class="services">-Perfect Live Music for Private &amp; Corporate Events, Weddings and Dinner Music-</p>
    <div class="stitch stitch--bottom"></div>
  </section>
</main>
</body>
</html>
```